Outlast the Coming Storm - book cover

A book cover (front) to be used on print book. Book will be 5 inches by 8 inches. Also need the cover image (as jpg) for promotional purposes. Include company logo on cover - I've included a couple of versions. Include my name as author: Dr. Corliss Vandemeer

Title of book is:
Weathering Every Market Tide
(sub-title) through coaching clear reasoning

this can be a sub-sub title, or a call out or "burst" standing alone -
A survival guide for 21st century business

If you'd like some inspiration, check out my web page: www.mentorvale.com
The company colors are red, white and blue, but I think red might be too harsh - use with caution if you use it.
RGB values of the company are:
Blue: 0/66/105
Red: 190/30/45

Target Market(s)

Business / Professionals / Chief Executives of Companies with more than 1000 employees

Industry/Entity Type

Business

Font styles to use
Serif

Colors
0255a3
ffffff

Requirements
Must have
• The title should make them pause and say "I need to get this book if I want my company to survive another 20 years!"
Nice to have
• Some image that signifies the future and / or uncertainty. Should be abstract - not people, not technology (which could change and then make the book look old). If you'd like to make the design a wrap from front to back, that is fine. I am not sure what text will go on the back at this point, so I may have to come back to you in a few months for an update.

```html
<!DOCTYPE html>
<html lang="en">
<head>
<meta charset="utf-8">
<title>Weathering Every Market Tide – book cover</title>
<link rel="stylesheet" href="https://fonts.googleapis.com/css2?family=Bebas+Neue&family=Oswald:wght@300;400&family=EB+Garamond:wght@400&display=swap">
<style>
  :root {
    --navy: #1b3f66;
    --navy-deep: #0f2c4d;
    --white: #ffffff;
    --paper: #f4f5f7;
    --stage: #ececec;
    --ink: #2a2a2a;
    --glow: #f0a24a;
    --sketch: #d9dde2;
  }
  * { box-sizing: border-box; margin: 0; padding: 0; }
  html, body { width: 1200px; height: 800px; overflow: hidden; }
  body { background: var(--stage); position: relative; }

  .wrap { position: absolute; left: 205px; top: 100px; width: 790px; height: 600px; display: flex; box-shadow: 0 10px 30px rgba(0,0,0,.18); }

  /* back cover */
  .back { position: relative; width: 375px; height: 600px; background: var(--paper); overflow: hidden; }
  .back-sketch { position: absolute; inset: 0; background: radial-gradient(ellipse at 50% 55%, #ffffff 0%, var(--paper) 50%, var(--sketch) 100%); }
  .back-copy { position: absolute; left: 26px; right: 26px; top: 28px; font-family: "EB Garamond", serif; font-size: 10.6px; line-height: 1.32; color: var(--ink); text-align: justify; }
  .back-copy p + p { margin-top: 11px; }
  .back-title { position: absolute; left: 0; right: 0; top: 390px; text-align: center; font-family: "Bebas Neue", sans-serif; color: var(--navy); font-size: 40px; line-height: .95; }
  .back-tagline { position: absolute; left: 0; right: 0; top: 478px; text-align: center; font-family: "Oswald", sans-serif; font-weight: 300; font-size: 12px; color: var(--navy); }
  .back-brand { position: absolute; left: 0; right: 0; top: 530px; text-align: center; }

  /* spine */
  .spine { position: relative; width: 40px; height: 600px; background: var(--navy-deep); }
  .spine-title { position: absolute; left: 50%; top: 50%; transform: translate(-50%, -50%) rotate(90deg); white-space: nowrap; font-family: "Bebas Neue", sans-serif; font-size: 22px; color: var(--white); letter-spacing: 1px; }

  /* front cover */
  .front { position: relative; width: 375px; height: 600px; background: var(--white); overflow: hidden; }
  .front-band { position: absolute; left: 0; top: 0; width: 100%; height: 215px; background: var(--navy); }
  .front-title { position: absolute; left: 0; right: 0; top: 28px; text-align: center; font-family: "Bebas Neue", sans-serif; font-size: 62px; line-height: .9; color: var(--white); }
  .front-tagline { position: absolute; left: 0; right: 0; top: 162px; text-align: center; font-family: "Oswald", sans-serif; font-weight: 300; font-size: 15px; color: var(--white); }
  .front-subtitle { position: absolute; left: 0; right: 0; top: 232px; text-align: center; font-family: "Oswald", sans-serif; font-weight: 300; font-size: 23px; color: var(--navy); }
  .front-bulb { position: absolute; left: 120px; top: 275px; width: 255px; height: 325px; background: radial-gradient(ellipse at 55% 38%, #fbd18a 0%, var(--glow) 20%, #c9c3b9 45%, rgba(255,255,255,0) 72%); }
  .brand { font-family: "Oswald", sans-serif; font-weight: 400; font-size: 22px; color: var(--navy); display: inline-flex; align-items: center; gap: 7px; }
  .brand-dot { width: 9px; height: 9px; border-radius: 50%; background: var(--navy); }
  .front-brand { position: absolute; left: 24px; top: 478px; }
  .front-author { position: absolute; left: 24px; top: 514px; font-family: "Bebas Neue", sans-serif; font-size: 36px; color: var(--navy); }
</style>
</head>
<body>
  <div class="wrap">
    <section class="back">
      <div class="back-sketch" role="img" aria-label="Faint hand-drawn business planning sketches"></div>
      <div class="back-copy">
        <p>Every organization faces storms it cannot predict. Markets shift, customers change and the tools of today fade fast. The companies that last are not the ones with the best forecasts but the ones whose people think well under pressure. This book shows leaders how to build that capacity on purpose, with practical methods for teaching judgment, questioning and clear reasoning at every level of the workforce.</p>
        <p>Drawing on years of consulting with large enterprises, the author offers a plain roadmap for leaders who want their company still standing twenty years from now. Read it, share it and put it to work.</p>
      </div>
      <h2 class="back-title">Weathering Every<br>Market Tide</h2>
      <p class="back-tagline">A SURVIVAL GUIDE FOR 21ST CENTURY BUSINESS</p>
      <div class="back-brand"><span class="brand"><span class="brand-dot"></span>Mentorvale</span></div>
    </section>

    <div class="spine"><span class="spine-title">WEATHERING EVERY MARKET TIDE</span></div>

    <section class="front">
      <div class="front-band"></div>
      <h1 class="front-title">Weathering Every<br>Market Tide</h1>
      <p class="front-tagline">A SURVIVAL GUIDE FOR 21ST CENTURY BUSINESS</p>
      <div class="front-bulb" role="img" aria-label="Glowing vintage light bulb over faint business sketches"></div>
      <p class="front-subtitle">THROUGH COACHING CLEAR REASONING</p>
      <div class="front-brand"><span class="brand"><span class="brand-dot"></span>Mentorvale</span></div>
      <p class="front-author">Dr. Corliss Vandemeer</p>
    </section>
  </div>
</body>
</html>
```